Labels for Bees Wax Candles & Honey Jars

We need labels for jars of natural honey. Most of our jars are square and the labels about 2" by 2".

Also we make bees wax candles of various sizes. We wish to wrap th enables around the circular candles which are between 2" and 3" in diameter... thus another have inch per label so they can be attached adhesively. The candles also vary in height... therefor th enables need to be 1.5", 2" and 3" in height.

We ar elooking for a very artistic and simple label that may include vibrant colors.
The name of our company must be displayed.. Candles by Morrow and for the Honey.... Morrow's All Natural Honey
Updates

The labels will be used for both Honey Jars as well as Bees Wax candles. There will be various sizes but that is something that can be adjusted after the initial design is approved. The Honey Jars should read "Natural Honey by Morrow" and the Candle labels should read "Natural Bees Wax Candles by Morrow" I am interested in simple, colorful, legible, and arty labels that pertain to bees and the natural environment. Hope this helps. We may also use a similar design on our web page. The size of the label on the honey will be 2" by 2" and the candles will vary.

Target Market(s)

Individual that purchase natural and organic products.

Requirements
Must have
• Labels should be very creative but legible and the emphasis on the candles should be all natural bees wax and the emphasis on the honey should be all natural honey. We are talking about the same design but different sizes and names.
Nice to have
• brillant colors and artistic

```html
<!DOCTYPE html>
<html lang="en">
<head>
<meta charset="utf-8">
<title>Morrow's Labels</title>
<link rel="stylesheet" href="https://fonts.googleapis.com/css2?family=Italianno&display=swap">
<style>
  :root {
    --stage: #020609;
    --comb-light: #f3d466;
    --comb-mid: #e6bb45;
    --comb-line: #f8e27a;
    --frame: #2a241a;
    --ink: #0d0b08;
    --honey-cell: #a6dcea;
    --honey-cell-deep: #8fcfe0;
    --candle-cell: #ee6c3f;
    --candle-cell-deep: #e85d32;
  }
  html, body {
    margin: 0;
    padding: 0;
    width: 1200px;
    height: 1000px;
    overflow: hidden;
    background: var(--stage);
  }
  .canvas {
    position: relative;
    width: 1200px;
    height: 1000px;
    font-family: "Italianno", cursive;
    color: var(--ink);
  }
  .label {
    position: absolute;
    overflow: hidden;
  }
  .label--honey { left: 348px; top: 2px; width: 503px; height: 503px; }
  .label--candle { left: 264px; top: 525px; width: 671px; height: 465px; }

  .label__comb {
    position: absolute;
    inset: 0;
    background: radial-gradient(ellipse at center, var(--comb-light) 0%, var(--comb-mid) 100%);
    box-shadow: inset 0 0 0 3px var(--comb-line);
  }
  .label__frame {
    position: absolute;
    inset: 0;
    width: 100%;
    height: 100%;
  }
  .label__frame line { stroke: var(--frame); stroke-linecap: round; }
  .label__frame polygon { fill: var(--frame); }

  .label__motif {
    position: absolute;
    border-radius: 6px;
  }
  .label--honey .label__motif {
    left: 160px; top: 80px; width: 206px; height: 128px;
    background: linear-gradient(135deg, var(--honey-cell) 0%, var(--honey-cell-deep) 100%);
  }
  .label--candle .label__motif {
    left: 262px; top: 96px; width: 190px; height: 100px;
    background: linear-gradient(135deg, var(--candle-cell) 0%, var(--candle-cell-deep) 100%);
  }

  .label__name,
  .label__tagline {
    position: absolute;
    left: 0;
    width: 100%;
    text-align: center;
    margin: 0;
    font-weight: 400;
    line-height: 1;
    white-space: nowrap;
  }
  .label--honey .label__name { top: 222px; font-size: 118px; }
  .label--honey .label__tagline { top: 348px; font-size: 70px; }
  .label--candle .label__name { top: 242px; font-size: 112px; }
</style>
</head>
<body>
<main class="canvas">
  <section class="label label--honey">
    <div class="label__comb" role="img" aria-label="Honeycomb pattern background in golden yellow"></div>
    <svg class="label__frame" viewBox="0 0 503 503" aria-hidden="true">
      <line x1="44" y1="49" x2="458" y2="45" stroke-width="4"/>
      <line x1="50" y1="42" x2="48" y2="458" stroke-width="5"/>
      <line x1="452" y1="44" x2="453" y2="432" stroke-width="4"/>
      <polygon points="40,449 300,446 452,450 458,456 300,458 44,458"/>
    </svg>
    <div class="label__motif" role="img" aria-label="Two light blue honeycomb cells with a small bee and looping flight trail"></div>
    <h1 class="label__name">morrow's</h1>
    <p class="label__tagline">all natural honey</p>
  </section>

  <section class="label label--candle">
    <div class="label__comb" role="img" aria-label="Honeycomb pattern background in golden yellow"></div>
    <svg class="label__frame" viewBox="0 0 671 465" aria-hidden="true">
      <line x1="32" y1="41" x2="636" y2="44" stroke-width="4"/>
      <line x1="38" y1="36" x2="37" y2="424" stroke-width="5"/>
      <line x1="632" y1="40" x2="633" y2="410" stroke-width="4"/>
      <polygon points="30,416 380,412 634,415 640,422 380,424 34,424"/>
    </svg>
    <div class="label__motif" role="img" aria-label="Two orange honeycomb cells with a small bee and looping flight trail"></div>
    <h2 class="label__name">Candles by morrow</h2>
  </section>
</main>
</body>
</html>
```